Real Estate Sign 2

Our company is called Harwick Tolland Realty. We are a real estate development company. We need a sign that we are going to hang outside of our projects that says: Another project brought to you by Harwick Tolland Realty... For Sale....(213) 555-0847. At the very bottom is needs to say CaBRE# 04736291" We want the Harwick Tolland Realty to be sophisticated, fresh, simple. We do not have a logo so maybe one can be incorporated into the sign. Sign will be about 30"x24"

Industry/Entity Type

Real Estate

```html
<!DOCTYPE html>
<html lang="en">
<head>
<meta charset="utf-8">
<title>Harwick Tolland Realty – For Sale Sign</title>
<link rel="stylesheet" href="https://fonts.googleapis.com/css2?family=Raleway:wght@300;400&family=Cinzel:wght@700&family=Montserrat:wght@700&family=Libre+Caslon+Text&display=swap">
<style>
  :root {
    --metal-light: #f7f7f8;
    --metal-mid: #e4e5e7;
    --metal-dark: #b9bbbf;
    --frame-edge: #a9abb0;
    --brand-blue: #1d1fa6;
    --band-blue: #03248a;
    --band-text: #ececf0;
    --ink: #111111;
  }
  * { margin: 0; padding: 0; box-sizing: border-box; }
  html, body { width: 1200px; height: 960px; overflow: hidden; background: #ffffff; }

  .sign {
    position: relative;
    width: 1200px;
    height: 960px;
    background:
      repeating-linear-gradient(180deg, rgba(255,255,255,0.35) 0 1px, rgba(0,0,0,0.03) 1px 3px),
      linear-gradient(135deg, var(--metal-dark), var(--metal-light) 30%, var(--metal-mid) 60%, var(--metal-dark));
  }
  .sign-panel {
    position: absolute;
    left: 38px; top: 38px;
    width: 1124px; height: 884px;
    border: 2px solid var(--frame-edge);
    box-shadow: inset 0 0 6px rgba(0,0,0,0.15);
    background:
      repeating-linear-gradient(180deg, rgba(255,255,255,0.5) 0 1px, rgba(0,0,0,0.025) 1px 3px),
      linear-gradient(160deg, var(--metal-mid), var(--metal-light) 40%, #ffffff 55%, var(--metal-mid));
  }

  .intro, .brand-line, .status-text, .phone, .license {
    position: absolute;
    left: 0; width: 1200px;
    text-align: center;
    white-space: nowrap;
  }
  .intro {
    top: 92px;
    font-family: "Raleway", sans-serif;
    font-weight: 300;
    font-size: 50px;
    color: var(--ink);
  }
  .brand-line {
    font-family: "Cinzel", serif;
    font-weight: 700;
    font-size: 78px;
    letter-spacing: 2px;
    color: var(--brand-blue);
  }
  .brand-line.first { top: 205px; }
  .brand-line.second { top: 310px; }

  .status-band {
    position: absolute;
    left: 96px; top: 464px;
    width: 1008px; height: 214px;
    background: var(--band-blue);
  }
  .status-text {
    top: 478px;
    font-family: "Montserrat", sans-serif;
    font-weight: 700;
    font-size: 196px;
    line-height: 1;
    color: var(--band-text);
    text-shadow: 2px 2px 2px rgba(0,0,0,0.35);
  }
  .phone {
    top: 708px;
    font-family: "Libre Caslon Text", serif;
    font-size: 94px;
    line-height: 1.1;
    color: var(--ink);
  }
  .license {
    top: 834px;
    font-family: "Raleway", sans-serif;
    font-weight: 400;
    font-size: 30px;
    color: var(--ink);
  }
</style>
</head>
<body>
  <div class="sign">
    <div class="sign-panel"></div>
    <p class="intro">Another project brought to you by</p>
    <p class="brand-line first">HARWICK TOLLAND</p>
    <p class="brand-line second">REALTY</p>
    <div class="status-band"></div>
    <p class="status-text">FOR SALE</p>
    <p class="phone">(213) 555-0847</p>
    <p class="license">CaBRE# 04736291</p>
  </div>
</body>
</html>
```